Corporate Design für logopädische Praxis
Ein Design, wie ich es mir gewünscht habe, eine unkomplizierte, schnelle und konstruktive Kommunikation mit einem kreativen Designer - herzlichen Dank an turavon!
Zielgruppe
Ich gründe eine logopädische Praxis, die Sprachtherapie sowohl für Erwachsene als auch Kinder anbietet und damit ein Logo benötigt, das jede Altersgruppe anspricht und 'Morgenfeld' als fachliche und menschliche Qualitätszeit interpretiert.
Aufgabenstellung
Ich bevorzuge ein klares Design, welches das Wortspiel der 'Morgenfeld' im Idealfall aufgreift und den Patienten vermittelt, dass sowohl die fachliche Qualität der Behandlung als auch die Ebene von Empathie und Patientenorientierung im zwischenmenschlichen Umgang für die Praxis zentral sind.

```html
<!DOCTYPE html>
<html lang="de">
<head>
<meta charset="utf-8">
<title>Morgenfeld – Praxis für Logopädie</title>
<link href="https://fonts.googleapis.com/css2?family=Nunito:wght@300;400&family=Raleway:wght@300;400&display=swap" rel="stylesheet">
<style>
  :root{
    --mauve:#a58eac;
    --ink:#5f5866;
    --text:#3a3a3c;
    --muted:#7d7782;
    --paper:#ffffff;
    --stage:#404040;
    --sky:#fbfbfc;
    --wash:#f1eff3;
    --rule:#b9b3bd;
  }
  *{margin:0;padding:0;box-sizing:border-box}
  html,body{width:1200px;height:2760px;overflow:hidden}
  body{position:relative;background:var(--sky);font-family:"Raleway",sans-serif;color:var(--text)}

  .brand{position:absolute;display:flex;flex-direction:column;align-items:flex-end}
  .brand-name{font-family:"Nunito",sans-serif;font-weight:300;color:var(--mauve);line-height:1;white-space:nowrap}
  .brand-tag{font-family:"Nunito",sans-serif;font-weight:400;color:var(--ink);line-height:1;white-space:nowrap}

  .hero{position:absolute;left:0;top:0;width:1200px;height:977px;background:var(--sky)}
  .hero .brand{right:324px;top:440px}
  .hero .brand-name{font-size:104px;letter-spacing:1px}
  .hero .brand-tag{font-size:32px;letter-spacing:5px;margin-top:8px}

  .stage{position:absolute;left:0;top:977px;width:1200px;height:1783px;background:var(--stage)}

  .card{position:absolute;top:1035px;width:380px;height:246px;background:var(--paper);overflow:hidden}
  .card-front{left:191px}
  .card-back{left:628px}
  .card-front .brand{right:81px;top:104px}
  .card-back .brand{right:131px;top:52px}
  .card .brand-name{font-size:40px}
  .card .brand-tag{font-size:13.5px;letter-spacing:2px;margin-top:3px}
  .card-person{position:absolute;left:34px;top:149px;font-size:10.5px;line-height:15px;color:var(--muted)}
  .card-person .name{color:var(--ink);font-size:11px;letter-spacing:.3px}
  .card-person .addr{margin-top:18px}
  .card-contact{position:absolute;left:209px;top:149px;list-style:none;font-size:9px;line-height:16px;color:var(--muted)}

  .contact-row{display:flex;align-items:center;gap:8px;white-space:nowrap}
  .icon{width:11px;height:11px;flex:none}

  .letter{position:absolute;left:131px;top:1328px;width:938px;height:1327px;background:var(--paper);overflow:hidden}
  .letter .brand{right:76px;top:102px}
  .letter .brand-name{font-size:58px}
  .letter .brand-tag{font-size:20px;letter-spacing:3px;margin-top:4px}
  .sender-line{position:absolute;left:116px;top:262px;font-size:9px;color:var(--muted)}
  .recipient{position:absolute;left:116px;top:288px;font-size:15px;line-height:19px;color:var(--text);font-style:normal;font-weight:300}
  .fold{position:absolute;left:0;width:23px;height:1px;background:var(--text)}
  .fold-a{top:468px}
  .fold-b{top:938px}
  .salutation{position:absolute;left:116px;top:463px;font-size:14.5px;font-weight:300}
  .body-copy{position:absolute;left:116px;top:520px;width:700px;font-size:14.2px;line-height:18.9px;font-weight:300;hyphens:auto}
  .body-copy p+p{margin-top:18px}
  .closing{position:absolute;left:116px;top:937px;font-size:14.5px;font-weight:300}
  .signature{position:absolute;left:116px;top:990px;width:150px;height:80px;background:linear-gradient(90deg,rgba(30,60,130,.06),rgba(30,60,130,.02))}

  .letter-foot{position:absolute;left:0;bottom:0;width:938px;height:320px}
  .foot-cols{position:absolute;left:116px;top:1197px;display:flex;font-size:10.5px;line-height:24.5px;color:var(--muted);white-space:nowrap}
  .foot-col{padding-right:22px}
  .foot-col + .foot-col{border-left:1px solid var(--rule);padding-left:22px}
  .foot-col:nth-child(1){width:167px}
  .foot-col:nth-child(2){width:162px}
  .foot-col:nth-child(3){width:239px}
</style>
</head>
<body>

<section class="hero">
  <div class="brand">
    <span class="brand-name">Morgenfeld</span>
    <span class="brand-tag">Praxis für Logopädie</span>
  </div>
</section>

<section class="stage"></section>

<article class="card card-front">
  <div class="brand">
    <span class="brand-name">Morgenfeld</span>
    <span class="brand-tag">Praxis für Logopädie</span>
  </div>
</article>

<article class="card card-back">
  <div class="brand">
    <span class="brand-name">Morgenfeld</span>
    <span class="brand-tag">Praxis für Logopädie</span>
  </div>
  <div class="card-person">
    <div class="name">MAX MUSTERMANN</div>
    <div>Geschäftsführer</div>
    <div class="addr">Musterweg 13<br>54321 Musterdorf</div>
  </div>
  <ul class="card-contact">
    <li class="contact-row"><svg class="icon" viewBox="0 0 12 12"><circle cx="6" cy="6" r="5" fill="none" stroke="#a58eac"/><text x="6" y="8.5" font-size="6" text-anchor="middle" fill="#7d7782">t</text></svg>+49 (0)4711 2 38 46-0</li>
    <li class="contact-row"><svg class="icon" viewBox="0 0 12 12"><circle cx="6" cy="6" r="5" fill="none" stroke="#a58eac"/><text x="6" y="8.5" font-size="6" text-anchor="middle" fill="#7d7782">f</text></svg>+49 (0)4711 2 38 46-50</li>
    <li class="contact-row"><svg class="icon" viewBox="0 0 12 12"><circle cx="6" cy="6" r="5" fill="none" stroke="#a58eac"/><text x="6" y="8.5" font-size="6" text-anchor="middle" fill="#7d7782">m</text></svg>+49 (0)170 9 14 26 83</li>
    <li class="contact-row"><svg class="icon" viewBox="0 0 12 12"><circle cx="6" cy="6" r="5" fill="none" stroke="#a58eac"/><text x="6" y="8.5" font-size="6" text-anchor="middle" fill="#7d7782">e</text></svg>praxis@morgenfeld-logo.de</li>
    <li class="contact-row"><svg class="icon" viewBox="0 0 12 12"><circle cx="6" cy="6" r="5" fill="none" stroke="#a58eac"/><text x="6" y="8.5" font-size="6" text-anchor="middle" fill="#7d7782">w</text></svg>morgenfeld-logo.de</li>
  </ul>
</article>

<article class="letter">
  <div class="brand">
    <span class="brand-name">Morgenfeld</span>
    <span class="brand-tag">Praxis für Logopädie</span>
  </div>

  <div class="sender-line">Morgenfeld | Musterweg 13 | 54321 Musterdorf</div>
  <address class="recipient">Max Mustermann<br>Musterstr. 1<br>12345 Muster</address>

  <span class="fold fold-a"></span>
  <span class="fold fold-b"></span>

  <p class="salutation">Sehr geehrte Damen und Herren,</p>

  <div class="body-copy">
    <p>Lorem ipsum dolor sit amet, consetetur sadipscing elitr, sed diam nonumy eirmod tempor invidunt ut labore et dolore magna aliquyam erat, sed diam voluptua. At vero eos et accusam et justo duo dolores et ea rebum. Stet clita kasd gubergren, no sea takimata sanctus est Lorem ipsum dolor sit amet. Lorem ipsum dolor sit amet, consetetur sadipscing elitr, sed diam nonumy eirmod tempor invidunt ut labore et dolore magna aliquyam erat, sed diam voluptua. At vero eos et accusam et justo duo dolores et ea rebum. Stet clita kasd gubergren, no sea takimata sanctus est Lorem ipsum dolor sit amet. Lorem ipsum dolor sit amet, consetetur sadipscing elitr, sed diam nonumy eirmod tempor invidunt ut labore et dolore magna aliquyam erat, sed diam voluptua. At vero eos et accusam et justo duo dolores et ea rebum. Stet clita kasd gubergren, no sea takimata sanctus est Lorem ipsum dolor sit amet.</p>
    <p>Duis autem vel eum iriure dolor in hendrerit in vulputate velit esse molestie consequat, vel illum dolore eu feugiat nulla facilisis at vero eros et accumsan et iusto odio dignissim qui blandit praesent luptatum zzril delenit augue duis dolore te feugait nulla facilisi. Lorem ipsum dolor sit amet, consectetuer adipiscing elit, sed diam nonummy nibh euismod tincidunt ut laoreet dolore magna aliquam erat volutpat.</p>
    <p>Ut wisi enim ad minim veniam, quis nostrud exerci tation ullamcorper suscipit lobortis nisl ut aliquip ex ea commodo consequat. Duis autem vel eum iriure dolor in hendrerit in vulputate velit esse molestie consequat, vel illum dolore eu feugiat nulla facilisis at vero eros et accumsan et iusto odio dignissim qui blandit praesent luptatum zzril delenit augue duis dolore te feugait nulla facilisi.</p>
  </div>

  <p class="closing">Mit freundlichen Grüßen</p>
  <div class="signature" role="img" aria-label="Handschriftliche Unterschrift"></div>

  <svg class="letter-foot" viewBox="0 0 938 320" preserveAspectRatio="none" aria-hidden="true">
    <path d="M0 125 C 250 120 420 80 600 40 C 720 15 840 5 938 0 L938 320 L0 320 Z" fill="#f1eff3"/>
  </svg>

  <div class="foot-cols">
    <div class="foot-col">
      <div class="contact-row"><svg class="icon" viewBox="0 0 12 12"><circle cx="6" cy="6" r="5" fill="none" stroke="#a58eac"/><text x="6" y="8.5" font-size="6" text-anchor="middle" fill="#7d7782">t</text></svg>+49 (0)4711 2 38 46-0</div>
      <div class="contact-row"><svg class="icon" viewBox="0 0 12 12"><circle cx="6" cy="6" r="5" fill="none" stroke="#a58eac"/><text x="6" y="8.5" font-size="6" text-anchor="middle" fill="#7d7782">f</text></svg>+49 (0)4711 2 38 46-50</div>
      <div class="contact-row"><svg class="icon" viewBox="0 0 12 12"><circle cx="6" cy="6" r="5" fill="none" stroke="#a58eac"/><text x="6" y="8.5" font-size="6" text-anchor="middle" fill="#7d7782">e</text></svg>praxis@morgenfeld-logo.de</div>
      <div class="contact-row"><svg class="icon" viewBox="0 0 12 12"><circle cx="6" cy="6" r="5" fill="none" stroke="#a58eac"/><text x="6" y="8.5" font-size="6" text-anchor="middle" fill="#7d7782">w</text></svg>morgenfeld-logo.de</div>
    </div>
    <div class="foot-col">
      <div>MAX MUSTERMANN</div>
      <div>Geschäftsführer</div>
      <div>Musterweg 13</div>
      <div>54321 Musterdorf</div>
    </div>
    <div class="foot-col">
      <div>Stadtbank Nord</div>
      <div>IBAN: DE43 XXXX 0110 XXXX 0481 XX</div>
      <div>BIC: KRXXDE55XXX</div>
      <div>Geschäftsführer: Max Mustermann</div>
    </div>
    <div class="foot-col">
      <div>Ust. ID: DE2XX9XX10X</div>
      <div>HRB 1XX4XX</div>
      <div>Amtsgericht Saarbrücken</div>
      <div>Gesellschaftssitz: Schwalbach</div>
    </div>
  </div>
</article>

</body>
</html>
```